Business Card Design

An energy company designed around renewable energy and energy storage that focuses on providing its energy at points on the grid that reduce costs and add value to the system.

Industry/Entity Type

Business

Contact Information for Business Card

Martin Delacroix
Executive Vice President
41 K ST NE
Washington, DC 20017
240-555-0183
mdelacroix@harborvoltco.example

```html
<!DOCTYPE html>
<html lang="en">
<head>
<meta charset="utf-8">
<title>Harbor Volt Co — Business Card</title>
<link rel="stylesheet" href="https://fonts.googleapis.com/css2?family=Jost:wght@300;400;500&display=swap">
<style>
  :root {
    --lime: #8cc63f;
    --leaf: #2fb24a;
    --paper: #ffffff;
    --ink: #4a4a4a;
    --ink-soft: #6b6b6b;
    --icon: #6e6e6e;
    --backdrop: #dcdedd;
  }
  * { box-sizing: border-box; margin: 0; padding: 0; }
  html, body {
    width: 1200px; height: 834px; overflow: hidden;
    background: var(--backdrop);
    font-family: "Jost", "Futura", sans-serif;
  }
  .card {
    position: absolute; left: 110px; top: 137px;
    width: 980px; height: 560px;
    background: var(--paper);
    box-shadow: 0 14px 40px rgba(0,0,0,.18);
    overflow: hidden;
  }
  .brand-panel {
    position: absolute; left: 0; top: 0;
    width: 500px; height: 420px;
    background: var(--lime);
    display: flex; align-items: center; justify-content: center; gap: 18px;
  }
  .brand-mark { width: 46px; height: 46px; border-radius: 50%; background: var(--paper); }
  .brand-name {
    color: var(--paper); font-weight: 400; font-size: 34px; letter-spacing: 1px;
  }
  .stripe { position: absolute; left: 0; width: 100%; }
  .stripe--leaf { top: 432px; height: 12px; background: var(--leaf); }
  .stripe--band { top: 456px; height: 104px; background: var(--lime); }
  .details {
    position: absolute; left: 548px; top: 74px; width: 410px; color: var(--ink);
  }
  .person { display: flex; align-items: center; gap: 16px; }
  .person-icon { width: 48px; height: 48px; flex: none; }
  .person-name { font-size: 32px; font-weight: 500; line-height: 1.1; }
  .person-title { margin: 2px 0 0 64px; font-size: 20px; font-weight: 300; color: var(--ink-soft); }
  .contact { list-style: none; margin-top: 34px; }
  .contact li {
    display: flex; align-items: flex-start; gap: 22px;
    font-size: 22px; font-weight: 300; line-height: 1.35; margin-bottom: 8px;
  }
  .contact svg { width: 24px; height: 24px; flex: none; margin-top: 4px; }
</style>
</head>
<body>
  <main class="card">
    <section class="brand-panel">
      <span class="brand-mark"></span>
      <span class="brand-name">HARBORVOLTCO</span>
    </section>

    <div class="stripe stripe--leaf"></div>
    <div class="stripe stripe--band"></div>

    <section class="details">
      <div class="person">
        <svg class="person-icon" viewBox="0 0 48 48" aria-hidden="true">
          <circle cx="24" cy="24" r="24" fill="var(--icon)"/>
          <circle cx="24" cy="19" r="7.5" fill="#fff"/>
          <path d="M10 40c2-8 7-12 14-12s12 4 14 12z" fill="#fff"/>
        </svg>
        <h1 class="person-name">Martin Delacroix</h1>
      </div>
      <p class="person-title">Executive Vice President</p>

      <ul class="contact">
        <li>
          <svg viewBox="0 0 24 24" aria-hidden="true">
            <circle cx="12" cy="12" r="12" fill="var(--icon)"/>
            <path d="M12 5a4.5 4.5 0 0 0-4.5 4.5c0 3.2 4.5 8.5 4.5 8.5s4.5-5.3 4.5-8.5A4.5 4.5 0 0 0 12 5z" fill="#fff"/>
            <circle cx="12" cy="9.5" r="1.7" fill="var(--icon)"/>
          </svg>
          <span>41 K ST NE Washington,<br>DC 20017</span>
        </li>
        <li>
          <svg viewBox="0 0 24 24" aria-hidden="true">
            <circle cx="12" cy="12" r="12" fill="var(--icon)"/>
            <path d="M8.5 6.5l2 2.4-1.2 1.4c.8 1.7 2 2.9 3.5 3.7l1.4-1.2 2.4 2-1.3 1.8c-4.2-.4-7.4-3.6-7.9-7.9z" fill="#fff"/>
          </svg>
          <span>240-555-0183</span>
        </li>
        <li>
          <svg viewBox="0 0 24 24" aria-hidden="true">
            <circle cx="12" cy="12" r="12" fill="var(--icon)"/>
            <rect x="6" y="8" width="12" height="8.5" rx="1" fill="#fff"/>
            <path d="M6.5 8.5l5.5 4.2 5.5-4.2" fill="none" stroke="var(--icon)" stroke-width="1.2"/>
          </svg>
          <span>mdelacroix@harborvoltco.example</span>
        </li>
      </ul>
    </section>
  </main>
</body>
</html>
```